Hawaiian Entertainment Booking Business needs a logo design/business card

We need a logo design/business card for a Hawaii based entertainment company called "Malvera Studios". We book all types of entertainment--musicians, bands, hula dancers, fire-knife dancers, halau, etc. for venues, events, weddings, parties, conventions. We would like to see designs that are cool, artistic, yet classy.

Industry/Entity Type

Entertainment Industry

Contact Information for Business Card

Leilani Kahuenga
Malvera Studios, LLC
P.O. Box 47213
Honolulu, HI 96822
(808)555-0147

Colors
acd036

Requirements
Must have
• Must say somewhere on card: Entertainment Services
Nice to have
• Please highlight: Leilani Kahuenga

```html
<!DOCTYPE html>
<html lang="en">
<head>
<meta charset="utf-8">
<title>Malvera Studios – Business Card</title>
<link rel="stylesheet" href="https://fonts.googleapis.com/css2?family=Montserrat:wght@400;500;700&display=swap">
<style>
  :root {
    --backdrop: #e6e7e9;
    --card-white: #ffffff;
    --teal: #56bcbc;
    --ink-grey: #6d6e70;
    --panel-text: #ffffff;
    --icon-ink: #3fa9aa;
    --art-yellow: #e9c85a;
    --art-orange: #e58a3a;
    --art-brown: #8a6a3a;
    --bird: #6a4a40;
  }
  * { box-sizing: border-box; margin: 0; padding: 0; }
  html, body { width: 1200px; height: 873px; overflow: hidden; }
  body {
    background: var(--backdrop);
    font-family: "Montserrat", Arial, sans-serif;
    position: relative;
  }
  .card {
    position: absolute;
    width: 600px;
    height: 343px;
    background: var(--card-white);
    border-radius: 16px;
    overflow: hidden;
    box-shadow: 0 6px 18px rgba(0,0,0,0.18);
  }
  .card--front { left: 120px; top: 60px; }
  .card--back  { left: 480px; top: 470px; }

  /* logo block: 310 x 150 */
  .logo { position: absolute; width: 310px; height: 150px; }
  .card--front .logo { left: 145px; top: 96px; }
  .card--back .logo  { left: 56px;  top: 96px; }

  .logo__art {
    position: absolute;
    left: 0; top: 0;
    width: 68px; height: 128px;
    border-radius: 34px 34px 10px 10px;
    background: linear-gradient(100deg, var(--art-yellow) 0%, var(--art-orange) 45%, var(--art-brown) 65%, var(--teal) 100%);
  }
  .logo__name {
    position: absolute;
    left: 78px; top: 34px;
    font-weight: 500;
    font-size: 27px;
    line-height: 34px;
    color: var(--teal);
    white-space: nowrap;
  }
  .logo__tagline {
    position: absolute;
    left: 78px; top: 80px;
    font-weight: 500;
    font-size: 12.5px;
    letter-spacing: 0.6px;
    color: var(--ink-grey);
    white-space: nowrap;
  }
  .logo__rule {
    position: absolute;
    left: 78px; top: 100px;
    width: 232px; height: 2px;
    background: var(--teal);
  }
  .logo__flourish {
    position: absolute;
    left: 150px; top: 110px;
    width: 80px; height: 12px;
    border-radius: 6px;
    background: var(--teal);
    opacity: 0.5;
  }

  .accent-art { position: absolute; }
  .accent-art--birds {
    left: 232px; top: 4px; width: 56px; height: 16px;
    border-radius: 8px;
    background: linear-gradient(90deg, rgba(106,74,64,0.55), rgba(106,74,64,0.25));
  }
  .accent-art--butterfly-a {
    left: 212px; top: 20px; width: 14px; height: 12px;
    border-radius: 50%;
    background: var(--art-orange);
  }
  .accent-art--butterfly-b {
    left: 294px; top: 60px; width: 14px; height: 12px;
    border-radius: 50%;
    background: linear-gradient(90deg, #9b6fd0, #e06aa8);
  }

  /* back card stripes and panel */
  .stripe { position: absolute; top: 0; height: 100%; background: var(--teal); }
  .edge-stripes .stripe--a { left: 0;  width: 14px; }
  .edge-stripes .stripe--b { left: 20px; width: 5px; }
  .edge-stripes .stripe--c { left: 31px; width: 5px; }
  .panel-stripes .stripe--a { left: 385px; width: 5px; }
  .panel-stripes .stripe--b { left: 396px; width: 5px; }

  .contact-panel {
    position: absolute;
    left: 407px; top: 0;
    width: 193px; height: 100%;
    background: var(--teal);
    color: var(--panel-text);
  }
  .contact-panel__name {
    position: absolute;
    right: 18px; top: 26px;
    font-weight: 700;
    font-size: 11.5px;
    letter-spacing: 0.5px;
    text-transform: uppercase;
    white-space: nowrap;
  }
  .contact-panel__title {
    position: absolute;
    right: 34px; top: 42px;
    font-size: 10.5px;
    white-space: nowrap;
  }
  .contact-list {
    position: absolute;
    right: 12px; top: 168px;
    list-style: none;
  }
  .contact-list li {
    display: flex;
    align-items: flex-start;
    justify-content: flex-end;
    gap: 8px;
    font-size: 11px;
    line-height: 16px;
    margin-bottom: 8px;
    text-align: right;
    white-space: nowrap;
  }
  .contact-list .icon {
    flex: none;
    width: 16px; height: 16px;
    border-radius: 50%;
    background: rgba(255,255,255,0.85);
    display: flex; align-items: center; justify-content: center;
  }
</style>
</head>
<body>

  <section class="card card--front" aria-label="Card front">
    <div class="logo">
      <div class="logo__art" role="img" aria-label="Illustration of two surfboards, a tiki carving and a hula dancer"></div>
      <div class="logo__name">Malvera Studios</div>
      <div class="logo__tagline">ENTERTAINMENT SERVICES</div>
      <div class="logo__rule"></div>
      <div class="logo__flourish" role="img" aria-label="Decorative swirl ornament"></div>
    </div>
  </section>

  <section class="card card--back" aria-label="Card back">
    <div class="edge-stripes">
      <span class="stripe stripe--a"></span>
      <span class="stripe stripe--b"></span>
      <span class="stripe stripe--c"></span>
    </div>

    <div class="logo">
      <div class="logo__art" role="img" aria-label="Illustration of two surfboards, a tiki carving and a hula dancer"></div>
      <div class="logo__name">Malvera Studios</div>
      <div class="logo__tagline">ENTERTAINMENT SERVICES</div>
      <div class="logo__rule"></div>
      <div class="logo__flourish" role="img" aria-label="Decorative swirl ornament"></div>
      <div class="accent-art accent-art--birds" role="img" aria-label="Flock of small birds in flight"></div>
      <div class="accent-art accent-art--butterfly-a" role="img" aria-label="Orange butterfly"></div>
      <div class="accent-art accent-art--butterfly-b" role="img" aria-label="Small colourful butterflies"></div>
    </div>

    <div class="panel-stripes">
      <span class="stripe stripe--a"></span>
      <span class="stripe stripe--b"></span>
    </div>

    <div class="contact-panel">
      <div class="contact-panel__name">Leilani Kahuenga</div>
      <div class="contact-panel__title">Marketing Manager</div>
      <ul class="contact-list">
        <li><span>808-555-0147</span>
          <span class="icon"><svg width="8" height="10" viewBox="0 0 8 10"><rect x="1" y="0.5" width="6" height="9" rx="1.2" fill="none" stroke="var(--icon-ink)" stroke-width="1.2"/></svg></span></li>
        <li><span>lkahuenga@mailhub.net</span>
          <span class="icon"><svg width="10" height="8" viewBox="0 0 10 8"><rect x="0.5" y="0.5" width="9" height="7" rx="1" fill="var(--icon-ink)"/><path d="M0.8 1 L5 4.5 L9.2 1" fill="none" stroke="#fff" stroke-width="0.9"/></svg></span></li>
        <li><span>P.O. Box 47213<br>Honolulu, HI 96822</span>
          <span class="icon"><svg width="8" height="10" viewBox="0 0 8 10"><path d="M4 9.5 C1.5 6.5 0.5 5 0.5 3.6 A3.5 3.5 0 0 1 7.5 3.6 C7.5 5 6.5 6.5 4 9.5Z" fill="var(--icon-ink)"/><circle cx="4" cy="3.6" r="1.2" fill="#fff"/></svg></span></li>
      </ul>
    </div>
  </section>

</body>
</html>
```